AMAZING WEBSITE DESIGN NEEDED FOR MAID / CLEANING SERVICE

NOTE: This is Website Design Only - No coding required

Please submit your designs ASAP as we want to pick a winner and get started!

Hey,

We are looking for a new amazing website design for a maid or cleaning service.

They have a horrible website that we want turned into a masterpiece.

As you will see on their current site:

http://tidyharborco.examplehost.net/

They have a lot of stuff, very disorganized, and need help.

Here is what we need:

Colors: Same as current site, Orange, Gray, Black

Menu: Horizontal with same Menu items

Need a spot for a video on the homepage

Want content to be structured in a great format that is easy to read.

Want to highlight commercial and residential on the website homepage.

Also want a spot for customer testimonials

We want the site clean, professional, fresh and modern.

Please help by matching the logo design.

I look forward to your designs!
Updates

Hi All! Really appreciate your efforts and designs. I will be meeting with our client on Monday and will then be able to provide feedback after our meeting. If you have other ideas, please submit them. The more I can show him the better! Thanks!

Target Market(s)

The target market is residential home owners as well as commercial businesses who need cleaning on a regular basis.

This company cleans homes and offices for individuals.

Industry/Entity Type

Residential

Font styles to use
Sans Serif

Requirements
Must have
• Must match logo colors
Must have spot for video
Must have a clean look
Must have a bold look
Nice to have
• Highly visual
Should not have
• clutter
messy design
hard to read

```html
<!DOCTYPE html>
<html lang="en">
<head>
<meta charset="utf-8">
<title>Tidy Harbor — Quality Commercial &amp; Residential Cleaning</title>
<link href="https://fonts.googleapis.com/css2?family=Open+Sans:wght@300;400;600;700&family=Roboto+Slab:wght@700&display=swap" rel="stylesheet">
<style>
:root{
  --orange:#f07c14;
  --charcoal:#333333;
  --slate:#555555;
  --slate-dark:#474747;
  --ink:#222222;
  --text:#666666;
  --light:#e9e9e9;
  --paper:#ffffff;
  --card:#e2e2e2;
}
*{box-sizing:border-box;margin:0;padding:0}
html,body{width:1200px;height:2882px;overflow:hidden}
body{position:relative;font-family:"Open Sans",Arial,sans-serif;color:var(--text);background:var(--paper)}
.abs{position:absolute}

/* top utility menu */
.topbar{left:0;top:0;width:1200px;height:34px;background:var(--charcoal);display:flex;z-index:2}
.topbar a{flex:auto;color:#fff;font-size:13px;font-weight:600;text-decoration:none;display:flex;align-items:center;justify-content:center;border-right:1px solid #555}
.topbar a:last-child{border-right:0}

/* header */
.header{left:0;top:34px;width:1200px;height:128px;background:var(--paper)}
.brand{left:32px;top:20px;display:flex;align-items:center;gap:10px}
.brand-mark{width:40px;height:40px;background:var(--charcoal)}
.brand-name{font-size:32px;font-weight:700;color:var(--orange);letter-spacing:-.5px}
.brand-tag{left:54px;top:74px;font-size:11px;font-weight:700;color:var(--slate);font-style:italic}
.badge{left:440px;top:14px;width:116px;height:116px;border-radius:50%;background:radial-gradient(circle,#f2d36a 0%,#d9a92c 48%,#8a6412 62%,#1e1e1e 64%,#3a3a3a 100%)}
.consult{left:578px;top:36px;font-size:15px;color:var(--text)}
.consult b{font-size:29px;font-weight:700;color:var(--orange);margin-left:6px;vertical-align:-3px}
.mainnav{right:28px;top:86px;display:flex;gap:26px}
.mainnav a{font-size:13px;font-weight:600;color:var(--ink);text-decoration:none;text-transform:uppercase}
.mainnav a.active{color:var(--orange)}

/* hero */
.hero{left:0;top:162px;width:1200px;height:466px;
  background:
    radial-gradient(ellipse 200px 260px at 560px 300px,rgba(150,175,205,.85),rgba(150,175,205,0) 100%),
    radial-gradient(ellipse 170px 230px at 1000px 280px,rgba(110,160,40,.95),rgba(110,160,40,0) 100%),
    radial-gradient(ellipse 160px 120px at 760px 220px,rgba(90,90,95,.7),rgba(90,90,95,0) 100%),
    radial-gradient(ellipse 120px 90px at 80px 370px,rgba(235,130,40,.7),rgba(235,130,40,0) 100%),
    linear-gradient(180deg,#e9e6e0 0%,#dcd8d0 45%,#b9b3a8 75%,#8d877c 100%)}
.hero-caption{left:0;top:568px;width:1200px;height:46px;background:rgba(255,255,255,.75)}
.hero-caption h1{position:absolute;left:28px;top:6px;font-family:"Roboto Slab",Georgia,serif;font-size:26px;color:var(--ink)}
.hero-dots{right:24px;top:584px;display:flex;gap:5px}
.hero-dots span{width:14px;height:14px;background:#777}
.hero-dots span:first-child{background:var(--orange)}
.hero-rule{left:0;top:628px;width:1200px;height:6px;background:var(--orange)}

/* welcome */
.video{left:83px;top:675px;width:308px;height:198px;border:1px solid #ccc;
  background:
    radial-gradient(ellipse 70px 60px at 110px 80px,rgba(240,220,40,.9),rgba(240,220,40,0)),
    radial-gradient(ellipse 80px 60px at 220px 70px,rgba(250,250,250,.9),rgba(250,250,250,0)),
    linear-gradient(180deg,#5f5c52 0%,#8a877a 40%,#c9c6ba 70%,#777 100%)}
.video-bar{left:84px;top:842px;width:306px;height:30px;background:rgba(255,255,255,.92)}
.welcome-title{left:430px;top:676px;font-size:37px;font-weight:300;color:var(--charcoal)}
.welcome-title b{font-weight:600;color:var(--orange)}
.welcome-text{left:430px;top:724px;width:720px;font-size:12.4px;line-height:18px}
.btn-dark{left:430px;top:840px;width:142px;height:36px;background:var(--slate);color:#fff;border-radius:3px;font-size:13px;font-weight:600;display:flex;align-items:center;justify-content:center}

/* services */
.services{left:0;top:924px;width:1200px;height:488px;background:var(--slate)}
.services h2{position:absolute;left:0;top:40px;width:1200px;text-align:center;color:#fff;font-size:30px;font-weight:600}
.services h2 span{font-weight:300}
.service{top:1015px;width:283px;height:363px}
.service-head{height:47px;background:var(--orange);color:#fff;font-size:21px;font-weight:600;display:flex;align-items:center;justify-content:center}
.service-photo{position:relative;height:316px}
.service-plus{position:absolute;left:117px;top:68px}
.service-copy{position:absolute;left:14px;top:226px;width:255px;text-align:center;color:#fff;font-size:11.5px;line-height:15px;text-shadow:0 1px 2px rgba(0,0,0,.6)}
.photo-office{background:
  radial-gradient(ellipse 60px 200px at 220px 200px,rgba(120,140,165,.9),rgba(120,140,165,0)),
  linear-gradient(180deg,#9fb8d2 0%,#7391b2 30%,#4c6784 60%,#2a3644 85%,#1b2129 100%)}
.photo-home{background:
  radial-gradient(ellipse 110px 50px at 140px 200px,rgba(30,30,30,.8),rgba(30,30,30,0)),
  radial-gradient(ellipse 60px 70px at 70px 130px,rgba(100,115,130,.8),rgba(100,115,130,0)),
  linear-gradient(180deg,#e4e0d6 0%,#c9c3b6 35%,#8c877c 70%,#3e3b36 100%)}
.photo-event{background:
  radial-gradient(ellipse 120px 80px at 140px 200px,rgba(220,90,50,.7),rgba(220,90,50,0)),
  linear-gradient(180deg,#2e231c 0%,#5a3a22 25%,#a8602a 55%,#d07a34 80%,#b55a26 100%)}

/* why choose */
.why{left:0;top:1412px;width:1200px;height:380px;background:linear-gradient(90deg,#fff 0%,#fff 60%,#ececec 85%,#dcdcdc 100%)}
.why-scene{left:900px;top:1412px;width:300px;height:380px;background:radial-gradient(ellipse 120px 170px at 170px 190px,rgba(150,150,150,.35),rgba(150,150,150,0))}
.why-photo{left:40px;top:1424px;width:454px;height:368px;
  background:
    radial-gradient(ellipse 70px 80px at 170px 70px,rgba(232,196,140,.95),rgba(232,196,140,0)),
    radial-gradient(ellipse 80px 60px at 340px 150px,rgba(70,130,225,.9),rgba(70,130,225,0)),
    radial-gradient(ellipse 70px 50px at 60px 260px,rgba(60,110,210,.9),rgba(60,110,210,0)),
    radial-gradient(ellipse 120px 110px at 200px 260px,rgba(236,200,40,.95),rgba(236,200,40,0)),
    radial-gradient(ellipse 150px 120px at 210px 220px,rgba(120,180,60,.7),rgba(120,180,60,0)),
    radial-gradient(ellipse 190px 180px at 210px 200px,rgba(235,225,215,1),rgba(255,255,255,0))}
.why-copy{left:519px;top:1412px;width:650px;height:380px}
.why-copy h2{position:absolute;left:0;top:40px;font-size:33px;font-weight:300;color:var(--charcoal)}
.why-copy h2 b{font-weight:600}
.why-copy h3{position:absolute;left:0;font-size:20px;font-weight:400;color:var(--orange)}
.why-copy p{position:absolute;left:0;width:610px;font-size:12.4px;line-height:18px}
.btn-orange{left:519px;top:1735px;width:142px;height:34px;background:var(--orange);color:#fff;border-radius:3px;font-size:13px;font-weight:600;display:flex;align-items:center;justify-content:center}

/* eco + cause */
.promise{left:0;top:1792px;width:1200px;height:236px;background:var(--light)}
.eco-art{left:50px;top:1836px;width:160px;height:160px;border-radius:50%;background:radial-gradient(circle at 40% 40%,#7fd446,#3a9a24 55%,#1f6a18 80%,#17501a)}
.ribbon-art{left:636px;top:1822px;width:92px;height:180px;background:radial-gradient(ellipse 46px 90px at 46px 90px,#f2a9c0,#e589a8 70%,rgba(233,233,233,0) 100%)}
.divider{left:592px;top:1814px;width:2px;height:190px;background:#bbb}
.promise-text{top:1860px;font-size:21px;line-height:29px;color:var(--slate)}

/* testimonials */
.reviews-title{left:0;top:2050px;width:1200px;text-align:center;font-size:33px;font-weight:300;color:var(--charcoal)}
.reviews-title b{font-weight:600}
.quote{top:2114px;width:336px;height:154px;background:var(--card);border-radius:6px;padding:14px 16px;font-size:12px;line-height:17.6px}
.reviewer{top:2280px;display:flex;gap:12px;align-items:flex-start}
.avatar{width:38px;height:38px;background:#cfcfcf;border:1px solid #bbb}
.reviewer b{display:block;font-size:14.5px;font-weight:400;color:var(--ink)}
.reviewer small{font-size:11px;color:#888}

/* call band */
.callband{left:0;top:2353px;width:1200px;height:79px;background:var(--slate-dark)}
.callband .ask{position:absolute;left:138px;top:28px;color:#fff;font-size:18px;font-weight:600}
.callband .phone{position:absolute;left:396px;top:17px;color:#fff;font-size:34px;font-weight:600}
.callband .sep{position:absolute;left:652px;top:18px;width:2px;height:44px;background:#777}
.callband .connect{position:absolute;left:668px;top:28px;color:#fff;font-size:18px;font-weight:600}
.social{position:absolute;left:852px;top:26px;display:flex;gap:4px}
.social span{width:26px;height:26px;background:#fff}

/* map */
.map{left:0;top:2432px;width:1200px;height:292px;background:linear-gradient(135deg,#dcdcdc,#ececec 50%,#d4d4d4)}
.map-card{left:389px;top:2454px;width:460px;height:102px;background:#fff;box-shadow:0 2px 6px rgba(0,0,0,.2);display:flex}
.map-brand{width:200px;display:flex;flex-direction:column;align-items:center;justify-content:center;gap:4px;border-right:1px solid #ccc}
.map-brand .name{font-size:22px;font-weight:700;color:var(--orange);display:flex;align-items:center;gap:6px}
.map-brand .name i{width:22px;height:22px;background:var(--charcoal)}
.map-brand small{font-size:8px;font-weight:700;color:var(--slate)}
.map-info{padding:10px 12px;font-size:11px;line-height:16px;color:#444}
.pin-label{left:608px;top:2604px;font-size:12px;color:#333;font-weight:600;line-height:15px}

/* footer */
.footer{left:0;top:2724px;width:1200px;height:158px;background:var(--orange);color:#fff}
.payline{position:absolute;left:0;top:32px;width:1200px;display:flex;justify-content:center;align-items:center;gap:6px;font-size:12px;font-weight:600}
.payline span{width:34px;height:22px;background:#fff;border-radius:2px}
.payline em{font-style:normal;margin-right:12px}
.footer-rule{position:absolute;left:20px;top:74px;width:1160px;height:1px;background:rgba(255,255,255,.5)}
.footlinks{position:absolute;left:0;top:86px;width:1200px;text-align:center;font-size:11.5px}
.footlinks a{color:#fff;text-decoration:underline}
.copy{position:absolute;left:0;top:114px;width:1200px;text-align:center;font-size:11.5px}
.copy a{color:#fff}
</style>
</head>
<body>

<nav class="topbar abs">
  <a>Our Services</a><a>Our Employees</a><a>Why choose Tidy Harbor?</a><a>What Our Customers Are Saying</a><a>Special Offers</a><a>Meet the President &amp; CEO</a>
</nav>

<header class="header abs">
  <div class="brand abs"><span class="brand-mark"></span><span class="brand-name">Tidy Harbor</span></div>
  <div class="brand-tag abs">Quality Commercial &amp; Residential Cleaning</div>
  <div class="badge abs" role="img" aria-label="Satisfaction guarantee seal"></div>
  <div class="consult abs">Call us Today and schedule your FREE consultation <b>(505) 555-0187</b></div>
  <nav class="mainnav abs"><a class="active">Home</a><a>About Us</a><a>Contact Us</a><a>Request a Bid</a></nav>
</header>

<section>
  <div class="hero abs" role="img" aria-label="Smiling housekeeper in yellow gloves cleaning a bright modern kitchen"></div>
  <div class="hero-caption abs"><h1>Wouldn't it be nice, To come home to a perfectly clean house?</h1></div>
  <div class="hero-dots abs"><span></span><span></span><span></span><span></span></div>
  <div class="hero-rule abs"></div>
</section>

<section>
  <div class="video abs" role="img" aria-label="Introduction video still of a gloved hand spraying a kitchen counter"></div>
  <div class="video-bar abs">
    <svg width="306" height="30" viewBox="0 0 306 30">
      <rect x="10" y="9" width="4" height="12" fill="#444"/><rect x="17" y="9" width="4" height="12" fill="#444"/>
      <rect x="32" y="13" width="230" height="5" fill="#999"/>
      <rect x="32" y="13" width="90" height="5" fill="#f07c14"/>
      <path d="M276 12h5l6-5v16l-6-5h-5z" fill="#444"/>
      <path d="M290 10q5 5 0 10" stroke="#444" stroke-width="2" fill="none"/>
    </svg>
  </div>
  <h2 class="welcome-title abs">WELCOME TO <b>Tidy Harbor</b></h2>
  <p class="welcome-text abs">Thank you for visiting us! You are one step closer to experiencing first class maid service! Our company specializes in detailed housekeeping, janitorial, and commercial cleaning services making your environment shine and sparkle like it never has before! Our maids are fully trained professionals who we recruit from high end luxury hotels we know, like the Grand Larkspur and Seaview Suites! We pride ourselves in delivering exceptional service to our valued customers by fully understanding what your expectations &amp; needs are! We will strive for perfection and we will provide an uncompromising commitment to excellence!</p>
  <div class="btn-dark abs">read more...</div>
</section>

<section class="services abs">
  <h2>Tidy Harbor's <span>Services</span></h2>
</section>
<div class="service abs" style="left:122px">
  <div class="service-head">Commercial &amp; Office</div>
  <div class="service-photo photo-office" role="img" aria-label="Glass office towers against a blue sky">
    <svg class="service-plus" width="50" height="50" viewBox="0 0 50 50"><circle cx="25" cy="25" r="25" fill="#333" opacity=".85"/><path d="M25 14v22M14 25h22" stroke="#fff" stroke-width="3"/></svg>
    <p class="service-copy">Isn't easier to work in a nice clean office? We will make your facility sparkle like new so your guests and clients have a nice clean area when they visit!</p>
  </div>
</div>
<div class="service abs" style="left:460px">
  <div class="service-head">Residential</div>
  <div class="service-photo photo-home" role="img" aria-label="Tidy living room with sofa and coffee table">
    <svg class="service-plus" width="50" height="50" viewBox="0 0 50 50"><circle cx="25" cy="25" r="25" fill="#333" opacity=".85"/><path d="M25 14v22M14 25h22" stroke="#fff" stroke-width="3"/></svg>
    <p class="service-copy">Isn't easier to work in a nice clean office? We will make your facility sparkle like new so your guests and clients have a nice clean area when they visit!</p>
  </div>
</div>
<div class="service abs" style="left:797px">
  <div class="service-head">Special Events</div>
  <div class="service-photo photo-event" role="img" aria-label="Confetti scattered across a party floor">
    <svg class="service-plus" width="50" height="50" viewBox="0 0 50 50"><circle cx="25" cy="25" r="25" fill="#333" opacity=".85"/><path d="M25 14v22M14 25h22" stroke="#fff" stroke-width="3"/></svg>
    <p class="service-copy">Isn't easier to work in a nice clean office? We will make your facility sparkle like new so your guests and clients have a nice clean area when they visit!</p>
  </div>
</div>

<section class="why abs"></section>
<div class="why-scene abs" role="img" aria-label="Faded housekeeper folding towels in the background"></div>
<div class="why-photo abs" role="img" aria-label="Cheerful cleaner holding a bucket of brushes and a feather duster"></div>
<div class="why-copy abs">
  <h2>Why Choose <b>Tidy Harbor?</b></h2>
  <h3 style="top:96px">Residential</h3>
  <p style="top:124px">Your Home! This is a sacred place, of peace, family, love, and memories! Let us give you more time for more happy memories!</p>
  <h3 style="top:166px">Commercial</h3>
  <p style="top:194px">Your Office! First Impressions are important! Set the stage with your clients in a sparkling office building!</p>
  <h3 style="top:238px">Property Management</h3>
  <p style="top:266px">A study recently released by the Southwest Home Owners Council said that 1 in 10 buyers and/or renters did not buy or rent a property simply because it was not clean, presentable.</p>
</div>
<div class="btn-orange abs">read more...</div>

<section class="promise abs"></section>
<div class="eco-art abs" role="img" aria-label="Eco friendly globe emblem"></div>
<p class="promise-text abs" style="left:233px;width:350px">Tidy Harbor is commited to using Eco Green chemicals to keep you and your family safe! No harsh chemicals here!</p>
<div class="divider abs"></div>
<div class="ribbon-art abs" role="img" aria-label="Pink awareness ribbon"></div>
<p class="promise-text abs" style="left:758px;width:400px">Tidy Harbor proudly donates 1% of its earnings to find a cure for breast cancer! Be part of a life changing cause!</p>

<h2 class="reviews-title abs">What our <b>Customers</b> are Saying!</h2>
<div class="quote abs" style="left:75px">" Tidy Harbor certainly takes away the daily headache of my household duties and gives me more time to spend with mychildren and husband. I am truly grateful to have someone who I can trust in my home. It has been an absolute pleasure to work with them. The affordability for their unlimited service is just amazing"</div>
<div class="quote abs" style="left:432px">" Tidy Harbor certainly takes away the daily headache of my household duties and gives me more time to spend with mychildren and husband. I am truly grateful to have someone who I can trust in my home. It has been an absolute pleasure to work with them. The affordability for their unlimited service is just amazing"</div>
<div class="quote abs" style="left:788px">" Tidy Harbor certainly takes away the daily headache of my household duties and gives me more time to spend with mychildren and husband. I am truly grateful to have someone who I can trust in my home. It has been an absolute pleasure to work with them. The affordability for their unlimited service is just amazing"</div>
<div class="reviewer abs" style="left:75px"><span class="avatar"></span><div><b>Dana Whitfield, Rio Rancho NM</b><small>March 25, 2014</small></div></div>
<div class="reviewer abs" style="left:432px"><span class="avatar"></span><div><b>Dana Whitfield, Rio Rancho NM</b><small>March 25, 2014</small></div></div>
<div class="reviewer abs" style="left:788px"><span class="avatar"></span><div><b>Dana Whitfield, Rio Rancho NM</b><small>March 25, 2014</small></div></div>

<section class="callband abs">
  <span class="ask">New Help Planning? Call us!</span>
  <span class="phone">(505) 555-0187</span>
  <span class="sep"></span>
  <span class="connect">Connect with us on</span>
  <div class="social"><span></span><span></span><span></span><span></span><span></span></div>
</section>

<section>
  <div class="map abs" role="img" aria-label="Street map of the office neighborhood in Albuquerque"></div>
  <div class="map-card abs">
    <div class="map-brand"><span class="name"><i></i>Tidy Harbor</span><small>Quality Commercial &amp; Residential Cleaning</small></div>
    <div class="map-info">4120 Mesa Verde Road NE, Suite 310<br>Albuquerque | New Mexico | 87109<br>(505) 555-0187 Office<br>(505) 555-0192 Fax<br>hello@tidyharbor.example</div>
  </div>
  <svg class="abs" style="left:584px;top:2562px" width="22" height="58" viewBox="0 0 22 58"><path d="M11 0v40" stroke="#555" stroke-width="3"/><path d="M3 34l8 22 8-22z" fill="#555"/></svg>
  <div class="pin-label abs">4120 Mesa<br>Verde Rd NE #310</div>
</section>

<footer class="footer abs">
  <div class="payline"><em>For your convienence we accept these major credit and debit cards for payment</em><span></span><span></span><span></span><span></span><span></span></div>
  <div class="footer-rule"></div>
  <div class="footlinks"><a>Home</a> | <a>Our Services</a> | <a>Our Employees</a> | <a>Why Choose Tidy Harbor?</a> | <a>What Our Customers are Saying</a> | Special Offers | <a>About Us</a> | <a>Contact Us</a> | <a>Request a Bid</a> | <a>Meet the President &amp; CEO</a></div>
  <div class="copy">© Copyright Tidy Harbor. All Rights Reserved. <a>Faq</a> &nbsp;<a>Privacy</a> &nbsp;<a>Terms &amp; Conditions</a></div>
</footer>

</body>
</html>
```